Label for Fatburner Metabolic Nutritial Supplement

We need a label design for our nutritial.
The product is fatburner. Incredients are green coffee, green tea and guarana.
The brand logo is "KLAVYN" (please see attachment).
The products name will be "amber v-tonic"
The size of the label must be 60 x 165 mm.
Besides the brand and the product name, there are a lot of further information, which must be on the label.
The bottle on wich the label will be sticked, consists of white plasic (see attachment)
Please find attached an excel document, which contails all the informations, which must be on the label. The grey area on the sample is for an barcode.
Also attached there is a first sample on how the label should be structured. Don't use this sample as a design guide, just use it to get an idea on how the informations (according to the excel sheet) can be fit on the label.
The attached font is for the KLAVYN logo only (if you need it)
We expect .ai, .psd and .pdf
Updates
The attached font is for the KLAVYN logo only (if you need it) Added Tuesday, May 10, 2016

```html
<!DOCTYPE html>
<html lang="de">
<head>
<meta charset="utf-8">
<title>amber v-tonic – Etikett</title>
<link href="https://fonts.googleapis.com/css2?family=Questrial&family=Exo+2:wght@500;600&display=swap" rel="stylesheet">
<style>
  :root {
    --teal-light: #8dd3c8;
    --teal-dark: #16a98d;
    --teal-note-text: #7be1cc;
    --lime: #8cc63f;
    --brand-blue: #3a7dc0;
    --text: #555a5c;
    --grey-box: #d1d3d4;
    --badge: #dfe7d6;
    --paper: #ffffff;
    --canvas: #eef1f1;
  }
  * { margin: 0; padding: 0; box-sizing: border-box; }
  html, body { width: 1200px; height: 1000px; overflow: hidden; background: var(--canvas); }
  body { position: relative; font-family: "Questrial", Arial, sans-serif; color: var(--text); }

  .label {
    position: absolute; left: 66px; top: 306px;
    width: 1070px; height: 387px;
    background: var(--paper); overflow: hidden;
    border: 1px solid #9aa3a5;
  }
  .label__top-band { position: absolute; left: 0; top: 0; width: 100%; height: 15px; background: var(--teal-light); }
  .label__waves { position: absolute; left: 0; top: 0; }

  .block { position: absolute; font-size: 10.5px; line-height: 13.5px; }
  .block h3 { font-weight: 400; font-size: 12.5px; text-decoration: underline; line-height: 14px; }
  .usage { left: 19px; top: 20px; width: 262px; }
  .note { left: 19px; top: 75px; width: 300px; }
  .ingredients { left: 19px; top: 174px; width: 290px; }
  .maker { left: 19px; top: 252px; width: 230px; }

  .certificate-badge {
    position: absolute; left: 256px; top: 228px;
    width: 58px; height: 58px; border-radius: 50%;
    background: var(--badge);
  }

  .brand {
    position: absolute; left: 464px; top: 36px;
    font-family: "Exo 2", sans-serif; font-weight: 600;
    font-size: 25px; letter-spacing: 0.5px; color: var(--brand-blue);
  }
  .product-name {
    position: absolute; left: 394px; top: 184px;
    font-family: "Exo 2", sans-serif; font-weight: 500;
    font-size: 40px; color: var(--lime); letter-spacing: 0.5px;
  }
  .category {
    position: absolute; left: 396px; top: 280px;
    font-family: "Exo 2", sans-serif; font-weight: 500;
    font-size: 17.5px; color: var(--lime);
  }
  .content-count {
    position: absolute; left: 461px; top: 357px;
    font-family: "Exo 2", sans-serif; font-weight: 500;
    font-size: 15px; color: var(--teal-dark);
  }
  .barcode-area { position: absolute; left: 19px; top: 321px; width: 205px; height: 52px; background: var(--grey-box); }

  .facts-title { position: absolute; right: 14px; top: 19px; font-size: 12.5px; text-decoration: underline; }
  .facts { position: absolute; left: 763px; top: 46px; width: 292px; font-size: 10.5px; line-height: 13.5px; }
  .facts__head { position: relative; height: 30px; border-bottom: 1.5px solid var(--teal-light); }
  .facts__head span { position: absolute; top: 0; }
  .facts__divider { position: absolute; left: 121px; top: 0; width: 1.5px; height: 108px; background: var(--teal-light); }
  .facts__names { position: absolute; left: 4px; top: 36px; }
  .facts__values { position: absolute; left: 149px; top: 36px; }

  .rm-note {
    position: absolute; left: 753px; top: 180px; width: 301px; height: 49px;
    background: var(--teal-dark); color: var(--teal-note-text); font-size: 10.5px; line-height: 13.5px;
    text-align: center; padding-top: 3px;
  }
  .fill-amount { position: absolute; left: 753px; top: 256px; font-size: 11px; color: var(--teal-dark); }
  .storage { left: 753px; top: 307px; width: 310px; }
</style>
</head>
<body>
  <div class="label">
    <div class="label__top-band"></div>
    <svg class="label__waves" width="1070" height="387" viewBox="0 0 1070 387">
      <path d="M0 312 C 200 318, 380 330, 520 324 C 700 316, 880 290, 1070 300 L1070 387 L0 387 Z" fill="var(--teal-light)"/>
      <path d="M0 303 C 180 300, 340 305, 480 332 C 360 332, 220 328, 0 322 Z" fill="var(--teal-dark)"/>
      <path d="M300 328 C 460 322, 640 300, 820 296 C 920 294, 1000 300, 1070 304 L1070 310 C 980 304, 880 302, 780 306 C 620 312, 470 330, 300 328 Z" fill="#ffffff" opacity="0.85"/>
    </svg>

    <div class="block usage">
      <h3>Verzehrempfehlung:</h3>
      <p>Drei Kapseln pro Tag mit ausreichend Flüssigkeit<br>einnehmen.</p>
    </div>
    <div class="block note">
      <h3>Hinweis:</h3>
      <p>Die angegebene empfohlene tägliche Verzehrsmenge.<br>darf nicht überschritten werden.<br>Nahrungsergänzungsmittel sollten nicht als Ersatz.<br>Für eine ausgewogene, abwechslungsreiche Ernährung.<br>Und gesunde Lebensweise verwendet werden.</p>
    </div>
    <div class="block ingredients">
      <h3>Zutaten:</h3>
      <p>Grüner Kaffee Extrakt, L-Carnitintartrat, Gurana Extrakt,<br>Überzugsmittel Hydroxypropylmethylcellulose, Grüntee<br>Extrakt Pfeffer schwarz</p>
    </div>
    <div class="block maker">
      <p>Herbaris Nutrition GmbH<br>Produkt: Delta Kapsel • Rezeptur: 27481.03<br>Datum: 14.09.16 KM</p>
    </div>
    <div class="certificate-badge" role="img" aria-label="Zertifizierungssiegel"></div>

    <div class="brand">KLAVYN</div>
    <div class="product-name">amber v-tonic</div>
    <div class="category">Nahrungsergänzungsmittel</div>
    <div class="content-count">Inhalt 90 Kapseln</div>
    <div class="barcode-area"></div>

    <div class="facts-title">Delta Kapsel &nbsp; - Nahrungsergänzungsmittel</div>
    <div class="facts">
      <div class="facts__head">
        <span style="left:4px">Zusammensetzung</span>
        <span style="left:143px">pro Tagesdosis<br>&nbsp;&nbsp;&nbsp;(3 Kapsel)</span>
        <span style="left:249px">RM (%)</span>
      </div>
      <div class="facts__divider"></div>
      <div class="facts__names">Grüner Kaffee Extrakt<br>Carnitintartrat<br>Guarana Extrakt<br>Grüntee Extrakt<br>Pfeffer, schwarz</div>
      <div class="facts__values">750.000 mg<br>600.000 mg<br>450.000 mg<br>300.00 &nbsp;mg<br>9.00 &nbsp;&nbsp;&nbsp;&nbsp;&nbsp;mg</div>
    </div>
    <div class="rm-note">RM (%): Referenzmengen für den druchschnittlichen<br>Erwachsenen nach der<br>Lebensmittelinformationsverordnung</div>
    <div class="fill-amount">Füllmenge: 73,8g (= 90Kapseln)</div>
    <div class="block storage">
      <h3>Aufbewahrung:</h3>
      <p>Das Produkt ist außerhalb der Reichweite von kleinen<br>Kindern aufzubewahren. Bitte lagern Sie das Produkt<br>trocken, lichtgeschützt und nicht über 25°C.</p>
      <p style="margin-top:6px">L.-Nr. / Mindestens haltbar bis Ende:</p>
    </div>
  </div>
</body>
</html>
```